We need a podcast cover design that will be used on Vexora. The podcast is called Founder Temperament Dial. The people we want to attract want us to be direct, real and upfront wiht them. They live in a noisy world and want clear and elegant design and funciton. We work with entrepreneurs who like brands like Quorla, Zentrix and Movari. We want a simple elegant design that uses the title on the cover along with the photo we uploaded. If someone goes to vexora, we want this to stand out and be visible.

Target Market(s)

Entrepreneurs, Artists, People who think differently

Industry/Entity Type

Consultant

Font styles to use
Sans Serif

Colors

Designer to choose colors to be used in the design.

Requirements
Must have
• The title on the podcast cover that will be legible on vExora. There should be high contrast so that the cover stands out on vexora with everyoe else.
Nice to have
• I would like to see the photo offset either right or left and bleeding off the page.
Should not have
• Too many colors, patterns or designs. Simple, elegant, and clean.

```html
<!DOCTYPE html>
<html lang="en">
<head>
<meta charset="UTF-8">
<title>Founder Temperament Dial — Podcast Cover</title>
<link href="https://fonts.googleapis.com/css2?family=Oswald:wght@400&family=Jost:ital,wght@1,500&display=swap" rel="stylesheet">
<style>
  :root {
    --paper: #ffffff;
    --band-blue: #1a72b9;
    --title-white: #ffffff;
    --photo-top: #eef0f1;
    --photo-skin: #d9bfae;
    --photo-shirt: #b5dbef;
  }
  html, body {
    margin: 0;
    padding: 0;
    width: 1200px;
    height: 1200px;
    overflow: hidden;
    background: var(--paper);
  }
  .cover {
    position: relative;
    width: 1200px;
    height: 1200px;
    background: var(--paper);
    overflow: hidden;
  }
  .host-portrait {
    position: absolute;
    left: 0;
    top: 0;
    width: 1200px;
    height: 849px;
    display: block;
  }
  .title-band {
    position: absolute;
    left: 0;
    top: 849px;
    width: 1200px;
    height: 351px;
    background: var(--band-blue);
  }
  .show-title {
    position: absolute;
    left: 0;
    width: 1200px;
    margin: 0;
    text-align: center;
    color: var(--title-white);
    font-family: "Oswald", "Arial Narrow", sans-serif;
    font-weight: 400;
    line-height: 1;
  }
  .show-title--main {
    top: 17px;
    font-size: 158px;
    letter-spacing: 1px;
  }
  .show-title--sub {
    top: 191px;
    left: 10px;
    font-size: 78px;
  }
  .host-credit {
    position: absolute;
    right: 376px;
    top: 287px;
    margin: 0;
    color: var(--title-white);
    font-family: "Jost", "Futura", sans-serif;
    font-style: italic;
    font-weight: 500;
    font-size: 27px;
    letter-spacing: 0.5px;
  }
</style>
</head>
<body>
  <main class="cover">
    <svg class="host-portrait" viewBox="0 0 1200 849" role="img" aria-label="Photo of the smiling podcast host in a light blue t-shirt, cut out on white, shoulders running into the title band">
      <defs>
        <linearGradient id="portrait-tone" x1="0" y1="0" x2="0" y2="1">
          <stop offset="0" stop-color="var(--photo-top)"/>
          <stop offset="0.45" stop-color="var(--photo-skin)"/>
          <stop offset="0.8" stop-color="var(--photo-shirt)"/>
        </linearGradient>
      </defs>
      <path d="M 50 849 C 70 730, 210 690, 340 650 L 310 300 C 300 120, 420 40, 530 40 C 650 40, 770 120, 760 300 L 730 650 C 900 680, 1080 730, 1105 849 Z" fill="url(#portrait-tone)"/>
    </svg>
    <section class="title-band">
      <h1 class="show-title show-title--main">Founder</h1>
      <p class="show-title show-title--sub">Temperament Dial</p>
      <p class="host-credit">with Dorian Kessel</p>
    </section>
  </main>
</body>
</html>
```